DL Gift Voucher

I need a DL sized gift voucher designed based on and incorporating my attached logo and the fonts therein. It should include the following elements:
Gift Certificate
To:_____________ (this should be a long line)
From:___________ (this should also be a long line)
Amount:________ (small line - enough for 4 digit number with dollar sign)
Authorised signature: ____ (small line)
Expiry Date: ________ (small line)
Ph. 0417 583 926
www.brambleoaklens.biz
Updates
Thank you to all the designers who have put the effort in to submit designs but I have pretty much chose one now. I'm sorry if you were eliminated - there were many great designs, it's a shame I can only choose one!

```html
<!DOCTYPE html>
<html lang="en">
<head>
<meta charset="utf-8">
<title>Bramble Oak Lens Gift Voucher</title>
<link rel="stylesheet" href="https://fonts.googleapis.com/css2?family=Crimson+Pro:wght@700&family=Arimo:wght@700&display=swap">
<style>
  :root {
    --red-deep: #a8141c;
    --red-main: #d9262e;
    --red-bright: #ee3a40;
    --red-dark: #6e0a10;
    --bow-red: #e8403a;
    --bow-mid: #c9262a;
    --bow-gold: #f2b640;
    --ink-white: #ffffff;
    --voucher-yellow: #ffd21f;
    --shadow-dark: #4a0508;
  }
  * { margin: 0; padding: 0; box-sizing: border-box; }
  html, body { width: 1200px; height: 601px; overflow: hidden; background: #ffffff; }
  .voucher {
    position: relative;
    width: 1200px;
    height: 601px;
    overflow: hidden;
    background:
      linear-gradient(200deg, var(--red-dark) 0%, rgba(110,10,16,0) 30%),
      radial-gradient(ellipse 70% 80% at 45% 55%, var(--red-bright) 0%, var(--red-main) 45%, var(--red-deep) 100%);
    font-family: "Crimson Pro", Georgia, serif;
    font-weight: 700;
    color: var(--ink-white);
  }
  .bow-art {
    position: absolute;
    left: 735px;
    top: 20px;
    width: 455px;
    height: 440px;
    border-radius: 48% 52% 45% 55% / 50% 45% 55% 50%;
    background:
      radial-gradient(circle at 40% 45%, rgba(242,182,64,0.45) 0%, rgba(242,182,64,0) 22%),
      radial-gradient(ellipse 60% 55% at 50% 50%, var(--bow-red) 0%, var(--bow-mid) 60%, rgba(201,38,42,0.6) 85%, rgba(201,38,42,0) 100%);
  }
  .fields { position: absolute; left: 39px; top: 0; }
  .field {
    position: absolute;
    left: 0;
    display: flex;
    align-items: baseline;
    white-space: nowrap;
    font-size: 32px;
    line-height: 1;
  }
  .field-line {
    flex: 1;
    border-bottom: 2px solid var(--ink-white);
    height: 0;
    margin-left: 2px;
  }
  .field-to { top: 83px; width: 671px; }
  .field-from { top: 152px; width: 678px; }
  .field-amount { top: 220px; width: 316px; }
  .field-signature { top: 287px; width: 600px; }
  .field-signature .field-line { margin-left: 6px; }
  .field-expiry { top: 358px; width: 357px; }
  .field-expiry .field-line { margin-left: 6px; }
  .banner { position: absolute; left: 0; top: 439px; width: 546px; height: 118px; }
  .banner-title {
    position: absolute;
    left: 41px;
    top: 456px;
    font-family: "Arimo", Arial, sans-serif;
    font-weight: 700;
    font-size: 64px;
    line-height: 1.2;
    color: var(--voucher-yellow);
    text-shadow: 3px 3px 0 var(--shadow-dark);
    letter-spacing: -1px;
  }
  .brand {
    position: absolute;
    left: 557px;
    top: 409px;
    width: 142px;
    height: 142px;
    border: 2px solid var(--ink-white);
    border-radius: 50%;
    display: flex;
    align-items: center;
    justify-content: center;
  }
  .brand-name {
    font-size: 24px;
    line-height: 1.1;
    text-align: center;
    color: var(--ink-white);
  }
  .contact {
    position: absolute;
    left: 743px;
    top: 486px;
    width: 440px;
    text-align: center;
    font-size: 30px;
    line-height: 40px;
  }
</style>
</head>
<body>
<main class="voucher">
  <div class="bow-art" role="img" aria-label="Large glossy red gift bow with gold-edged ribbon loops"></div>

  <section class="fields">
    <div class="field field-to">To:<span class="field-line"></span></div>
    <div class="field field-from">From:<span class="field-line"></span></div>
    <div class="field field-amount">Amount: $<span class="field-line"></span></div>
    <div class="field field-signature">Authorised signature:<span class="field-line"></span></div>
    <div class="field field-expiry">Expiry Date:<span class="field-line"></span></div>
  </section>

  <svg class="banner" viewBox="0 0 546 118" aria-hidden="true">
    <defs>
      <linearGradient id="bannerFill" x1="0" y1="0" x2="1" y2="0">
        <stop offset="0" stop-color="#b3121a"/>
        <stop offset="0.2" stop-color="#f4797b"/>
        <stop offset="0.5" stop-color="#e52a31"/>
        <stop offset="1" stop-color="#a90f17"/>
      </linearGradient>
      <linearGradient id="bannerTail" x1="0" y1="0" x2="1" y2="0">
        <stop offset="0" stop-color="#a9111a"/>
        <stop offset="1" stop-color="#6e0a10"/>
      </linearGradient>
    </defs>
    <polygon points="0,0 546,0 500,118 0,118" fill="url(#bannerTail)"/>
    <polygon points="0,0 520,0 485,118 0,118" fill="url(#bannerFill)"/>
  </svg>
  <div class="banner-title">Gift Voucher</div>

  <div class="brand">
    <span class="brand-name">Bramble<br>Oak Lens</span>
  </div>

  <div class="contact">
    <p>Ph. 0417 583 926</p>
    <p>www.brambleoaklens.biz</p>
  </div>
</main>
</body>
</html>
```